Business Card Design Project

I need a business card design for our new logo, please check the logo at the following link:
https://files.quorvane-share.com/s/p7tkwe3nq4zr81h/FernCove.png
The address on the business card:
Av. Olegário Tavares 418 sala 207
Barra da Tijuca, Rio de Janeiro, RJ
CEP: 24917-380
Brasil
Phone: +55 21 73408216
e-mail: rogerio@ferncove-exemplo.com.br
Updates
Thank you all for sending your designs, we will not provide feedback because there are too many designs, on December 3 we will pick the best design according to our point of view. Please keep posting.
Rogério
Industry/Entity Type
Business

```html
<!DOCTYPE html>
<html lang="pt-BR">
<head>
<meta charset="utf-8">
<title>FernCove – Business Card</title>
<link rel="stylesheet" href="https://fonts.googleapis.com/css2?family=Mulish:wght@400;700;800&display=swap">
<style>
  :root {
    --stage: #e9e6e1;
    --card-light: #6c6c6c;
    --card-mid: #4a4a4a;
    --card-dark: #2f2f2f;
    --ink: #1f1f1f;
    --accent: #f2e41c;
    --ghost: rgba(255,255,255,0.16);
    --figure: #262626;
  }
  * { margin: 0; padding: 0; box-sizing: border-box; }
  html, body { width: 1200px; height: 684px; overflow: hidden; }
  body {
    background: var(--stage);
    font-family: "Mulish", sans-serif;
    position: relative;
  }
  .card {
    position: absolute;
    top: 199px;
    width: 500px;
    height: 286px;
    overflow: hidden;
    box-shadow: 0 10px 24px rgba(0,0,0,0.28);
  }
  .card--front {
    left: 70px;
    background: radial-gradient(ellipse at 45% 15%, var(--card-light) 0%, var(--card-mid) 55%, var(--card-dark) 100%);
  }
  .card--back {
    left: 630px;
    background: radial-gradient(ellipse at 55% 10%, var(--card-light) 0%, var(--card-mid) 50%, var(--card-dark) 100%);
  }

  /* front */
  .mascot-art {
    position: absolute;
    left: 170px; top: 40px;
    width: 160px; height: 130px;
    background: radial-gradient(circle at 50% 50%, #3a3a3a 0%, var(--figure) 70%);
    border-radius: 14px;
  }
  .brand-name {
    position: absolute;
    left: 0; right: 0; top: 182px;
    text-align: center;
    font-weight: 800;
    font-size: 46px;
    letter-spacing: 0.5px;
    color: var(--ink);
  }

  /* back */
  .holder {
    position: absolute;
    left: 218px; top: 128px;
  }
  .holder__name {
    font-weight: 800;
    font-size: 28px;
    letter-spacing: 1px;
    color: var(--ink);
    line-height: 1;
  }
  .holder__role {
    font-weight: 700;
    font-size: 13px;
    color: var(--accent);
    margin-left: 12px;
  }
  .mascot-ghost {
    position: absolute;
    left: 330px; top: 120px;
    width: 120px; height: 100px;
    background: var(--ghost);
    border-radius: 14px;
  }
  .brand-ghost {
    position: absolute;
    left: 318px; top: 222px;
    font-weight: 800;
    font-size: 30px;
    color: var(--ghost);
  }
  .contact {
    position: absolute;
    left: 22px; top: 176px;
    padding-left: 8px;
    border-left: 3px solid var(--accent);
    font-size: 9px;
    line-height: 1.45;
    color: var(--accent);
  }
  .address {
    position: absolute;
    left: 22px; bottom: 22px;
    font-size: 8px;
    color: var(--accent);
    white-space: nowrap;
  }
</style>
</head>
<body>
  <section class="card card--front" aria-label="Business card front">
    <div class="mascot-art" role="img" aria-label="Mascot illustration: running figure with hat and briefcase"></div>
    <div class="brand-name">FernCove</div>
  </section>

  <section class="card card--back" aria-label="Business card back">
    <div class="mascot-ghost" role="img" aria-label="Faint mascot illustration"></div>
    <div class="brand-ghost">FernCove</div>
    <div class="holder">
      <div class="holder__name">NAME</div>
      <div class="holder__role">Designation</div>
    </div>
    <address class="contact" style="font-style:normal">
      rogerio@ferncove-exemplo.com.br<br>
      +55 21 73408216
    </address>
    <p class="address">Av. Olegário Tavares 418 sala 207 Barra da Tijuca, Rio de Janeiro, RJ CEP 24917-380 Brasil</p>
  </section>
</body>
</html>
```